Video Company Business Card Design

We are looking for a new design for business cards that will complement our new logo and new website design.

Target Market(s)

professionals who need video work done

Industry/Entity Type

Business

Requirements
Must have
• Logo
compliment website look seen here...http://k7pixelworks.example/brightlane/

info for card:
Dana Whitlow
Producer/ Cinematographer

532 Pellingham NE
Fenwick Bay, WA 98765
(inside The RAVN Hall)
(616) 555-0142
Dana@brightlanemedia.example
www.brightlanemedia.example

```html
<!DOCTYPE html>
<html lang="en">
<head>
<meta charset="utf-8">
<title>Brightlane Media Business Card</title>
<link href="https://fonts.googleapis.com/css2?family=Montserrat:wght@400;600;700&display=swap" rel="stylesheet">
<style>
  :root {
    --page: #f1f1f1;
    --card-black: #000000;
    --card-back: #1c1c1c;
    --card-edge: #c9c9c9;
    --brand-green: #3aaa4a;
    --band-light: #8fe08a;
    --band-dark: #2e9a3c;
    --text-white: #ffffff;
    --text-dark: #1a1a1a;
  }
  * { margin: 0; padding: 0; box-sizing: border-box; }
  html, body { width: 1200px; height: 848px; overflow: hidden; }
  body {
    background: var(--page);
    font-family: "Montserrat", Arial, sans-serif;
    position: relative;
  }
  .card {
    position: absolute;
    top: 194px;
    width: 471px;
    height: 282px;
    border-radius: 17px;
    border: 1px solid var(--card-edge);
    overflow: hidden;
  }
  .card-front { left: 95px; background: var(--card-black); }
  .card-back {
    left: 645px;
    background: radial-gradient(ellipse at 45% 40%, #292929 0%, var(--card-back) 70%);
  }
  .wordmark {
    position: absolute;
    left: 0; right: 0;
    text-align: center;
    font-weight: 700;
    font-size: 33px;
    letter-spacing: 0.5px;
    color: var(--brand-green);
    white-space: nowrap;
  }
  .card-front .wordmark { top: 38px; }
  .card-back .wordmark { top: 119px; }
  .contact {
    position: absolute;
    top: 108px; left: 0; right: 0;
    text-align: center;
    color: var(--text-white);
  }
  .contact-name { font-weight: 700; font-size: 17px; letter-spacing: 0.5px; }
  .contact-title { color: var(--brand-green); font-weight: 600; font-size: 12.5px; margin-top: 3px; letter-spacing: 0.3px; }
  .contact-lines { margin-top: 16px; font-size: 12.5px; line-height: 18px; }
  .contact-lines .label { color: var(--brand-green); font-weight: 600; }
  .contact-note { font-size: 8px; line-height: 10px; }
  .web-band {
    position: absolute;
    left: 0; right: 0; bottom: 0;
    height: 48px;
    border-top: 3px solid var(--brand-green);
    background: linear-gradient(to bottom, var(--band-light) 0%, var(--brand-green) 55%, var(--band-dark) 100%);
    display: flex;
    align-items: center;
    justify-content: center;
    font-size: 14.5px;
    letter-spacing: 2.5px;
    color: var(--text-dark);
  }
  .web-band strong { font-weight: 700; }
</style>
</head>
<body>
  <section class="card card-front" aria-label="Business card front">
    <div class="wordmark">BRIGHTLANE MEDIA</div>
    <div class="contact">
      <div class="contact-name">Dana Whitlow</div>
      <div class="contact-title">Producer/ Cinematographer</div>
      <div class="contact-lines">
        <div><span class="label">p:</span>&nbsp; 555.555.0142</div>
        <div><span class="label">e:</span>&nbsp; Dana@brightlanemedia.example</div>
        <div>532 Pellingham NE,&nbsp; Fenwick Bay, WA 98765</div>
      </div>
      <div class="contact-note">(inside The RAVN Hall)</div>
    </div>
    <div class="web-band">www.<strong>brightlanemedia</strong>.example</div>
  </section>

  <section class="card card-back" aria-label="Business card back">
    <div class="wordmark">BRIGHTLANE MEDIA</div>
  </section>
</body>
</html>
```